The Willow Cove Clinic - Instagram Photospot

We are looking for an instagram type wal for our pediatric dental office. We are thinking it could be weaved into a whole bunch of what we do (i.e. potentially water marked or faded in the background on letterhead, as an instragram type wall in the practice, as a banner or section of the home page on the website, on rack cards, etc.) I’m thinking it would utilize a nice fun cursive script for the wording "The Willow Cove Clinic is the spot for...." and a bunch of different sized “spots” with meaningful words that speak to who we are. That list would include things like:

• Fun
• Smiles
• Laughter
• Caring
• Comfort
• Amazing
• Kids
• Toddlers
• Teens
• Friends
• Family
• Health
• Education
• Cheer
• Positivity
• Exceptional Care

From a color perspective….we could look at a couple of options. We could have one version that has it washed out and in the background (more subliminal). We could have one version that was consistent with the colors in our logo. And we could have one version that popped with more color by utilizing the colors in some of the artwork we use throughout the office (snowboard picture as an example)

Target Market(s)

Appeal to hip families with kids

Industry/Entity Type

Pediatric Dental

Other font styles liked:
• something modern, hip, playful and fun

Colors
0054AA
0677BA
7BADD7
CADEEF
E8F1F8
0094D4
00A9DD
6FCCEA
C7EBF8
E9F6FB
00AB8E
00BBA5
67D7C9
C6EFE9
E9F9F6

Requirements
Must have
• Use of existing logo and a play on "spots" or polka dots with symbpolic wording. Must appeal to young parents and kiddos (including hip teens)
Should not have
• SHOULDNT BE OVER THE TOP KIDS.

```html
<!DOCTYPE html>
<html lang="en">
<head>
<meta charset="utf-8">
<title>The Willow Cove Clinic – Photo Wall</title>
<link rel="stylesheet" href="https://fonts.googleapis.com/css2?family=Fredoka:wght@600&family=Lobster&display=swap">
<style>
  :root {
    --page: #e7e8ea;
    --shadow: #d3d4d6;
    --wall-center: #8fe1ee;
    --wall-edge: #6ecbdc;
    --spot: #dc2344;
    --spot-ring: #c81d3c;
    --title: #f0425f;
    --badge: #18384e;
    --white: #ffffff;
    --deco-light: rgba(255, 255, 255, 0.35);
    --deco-teal: rgba(33, 190, 200, 0.45);
    --deco-red: rgba(240, 66, 95, 0.35);
  }
  * { box-sizing: border-box; margin: 0; padding: 0; }
  html, body { width: 1200px; height: 1200px; overflow: hidden; background: var(--page); }
  .canvas { position: relative; width: 1200px; height: 1200px; }
  .wall-shadow {
    position: absolute; left: 102px; top: 107px; width: 1028px; height: 1028px;
    background: var(--shadow);
  }
  .wall {
    position: absolute; left: 86px; top: 86px; width: 1028px; height: 1028px; overflow: hidden;
    background: radial-gradient(circle at 50% 50%, var(--wall-center) 0%, var(--wall-edge) 80%);
  }
  .deco {
    position: absolute; border-radius: 40px;
  }
  .deco--light { background: var(--deco-light); }
  .deco--teal { background: var(--deco-teal); }
  .deco--red { background: var(--deco-red); }

  .headline {
    position: absolute; left: 0; top: 282px; width: 1200px; text-align: center;
    font-family: "Lobster", cursive; font-size: 62px; line-height: 1;
    color: var(--title); letter-spacing: 0.5px;
  }

  .spot {
    position: absolute; border-radius: 50%;
    display: flex; align-items: center; justify-content: center; text-align: center;
    background: var(--spot);
    box-shadow: 0 0 0 1.5px var(--spot-ring), 2px 2px 0 2px rgba(200, 29, 60, 0.55);
    font-family: "Fredoka", sans-serif; font-weight: 600; color: var(--white);
    transform: translate(-50%, -50%); line-height: 1.1;
  }
  .spot--sm { width: 80px; height: 80px; font-size: 14px; }
  .spot--md { width: 82px; height: 82px; font-size: 22px; }
  .spot--lg { width: 102px; height: 102px; font-size: 24px; }
  .spot--xl { width: 120px; height: 120px; font-size: 30px; }
  .spot--xxl { width: 130px; height: 130px; font-size: 28px; }
  .spot--tiny-text { font-size: 10.5px; }

  .badge {
    position: absolute; left: 599px; top: 599px; width: 176px; height: 176px;
    transform: translate(-50%, -50%); border-radius: 50%; background: var(--badge);
    display: flex; align-items: center; justify-content: center;
    font-family: "Fredoka", sans-serif; font-weight: 600; color: var(--white);
    font-size: 17px; letter-spacing: 1px;
  }
</style>
</head>
<body>
<main class="canvas">
  <div class="wall-shadow"></div>
  <section class="wall">
    <div class="deco deco--light" role="img" aria-label="Dental illustrations: toothbrush, floss, teeth and mint leaves" style="left:0;top:0;width:360px;height:200px;"></div>
    <div class="deco deco--teal" role="img" aria-label="Dental illustrations: interdental brush and mouthwash bottle" style="left:380px;top:-20px;width:280px;height:120px;"></div>
    <div class="deco deco--light" role="img" aria-label="Dental illustrations: dental mirror and teeth" style="left:690px;top:0;width:338px;height:140px;"></div>
    <div class="deco deco--red" role="img" aria-label="Illustrated teeth with braces" style="left:900px;top:150px;width:128px;height:220px;"></div>
    <div class="deco deco--light" role="img" aria-label="Illustrated tooth" style="left:0;top:130px;width:110px;height:150px;"></div>
    <div class="deco deco--teal" role="img" aria-label="Toothpaste tube and water flosser illustrations" style="left:-20px;top:620px;width:140px;height:330px;"></div>
    <div class="deco deco--light" role="img" aria-label="Dentures, interdental brush, mint leaves and dental mirror" style="left:0;top:900px;width:400px;height:128px;"></div>
    <div class="deco deco--light" role="img" aria-label="Teeth, mint leaves and chewing gum illustrations" style="left:420px;top:960px;width:340px;height:90px;"></div>
    <div class="deco deco--teal" role="img" aria-label="Toothbrush, toothpaste and electric toothbrush illustrations" style="left:780px;top:700px;width:248px;height:328px;"></div>
  </section>

  <h1 class="headline">The Willow Cove Clinic is ...</h1>

  <div class="spot spot--sm" style="left:168px;top:442px;">Comfort</div>
  <div class="spot spot--sm" style="left:316px;top:484px;">Amazing</div>
  <div class="spot spot--sm" style="left:481px;top:440px;font-size:18px;">TEENS</div>
  <div class="spot spot--sm" style="left:679px;top:432px;">Education</div>
  <div class="spot spot--md" style="left:865px;top:463px;">KIDS</div>
  <div class="spot spot--sm" style="left:1009px;top:532px;">Laughter</div>
  <div class="spot spot--xxl" style="left:225px;top:602px;">Smiles</div>
  <div class="spot spot--sm" style="left:399px;top:631px;">Family</div>
  <div class="spot spot--sm" style="left:811px;top:581px;">Toddlers</div>
  <div class="spot spot--xl" style="left:939px;top:689px;">FUN</div>
  <div class="spot spot--sm" style="left:287px;top:758px;">Cheer</div>
  <div class="spot spot--sm spot--tiny-text" style="left:573px;top:774px;">Exceptional<br>Care</div>
  <div class="spot spot--sm" style="left:759px;top:736px;">Positivity</div>
  <div class="spot spot--sm" style="left:424px;top:853px;">Caring</div>
  <div class="spot spot--sm" style="left:824px;top:848px;">Friends</div>
  <div class="spot spot--lg" style="left:586px;top:928px;">Health</div>

  <div class="badge">WILLOW COVE</div>
</main>
</body>
</html>
```